Harborline Motors LLC

Car Dealer Customer Service
Address: 2741 Linden Avenue, Shelbyville, TN 37162
web: www.harborlinemotorstn.net
email: harborlinemotorstn@mailbox-example.net
Phone: (931) 555-0148
Phone: (629) 555-0173

```html
<!DOCTYPE html>
<html lang="en">
<head>
<meta charset="utf-8">
<title>Harborline Motors – Business Card</title>
<link rel="stylesheet" href="https://fonts.googleapis.com/css2?family=Montserrat:wght@700;800&family=Arimo:wght@400&display=swap">
<style>
  :root {
    --brand-blue: #1a78a8;
    --brand-blue-light: #2f8fc4;
    --brand-gold: #e9b040;
    --ink: #222222;
    --paper: #ffffff;
    --backdrop: #d6d6d6;
  }
  * { box-sizing: border-box; margin: 0; padding: 0; }
  html, body { width: 1200px; height: 800px; overflow: hidden; }
  body {
    background: var(--backdrop);
    display: flex;
    align-items: center;
    justify-content: center;
    gap: 40px;
    font-family: "Arimo", Arial, sans-serif;
  }
  .card {
    width: 560px;
    height: 320px;
    position: relative;
    border-bottom: 3px solid var(--brand-gold);
    border-left: 3px solid var(--brand-gold);
  }
  /* Contact side */
  .card--contact { background: var(--paper); }
  .contact__brand {
    position: absolute;
    top: 44px; right: 40px;
    display: flex; align-items: center; gap: 14px;
  }
  .brand-dot {
    width: 44px; height: 44px; border-radius: 50%;
    background: var(--brand-blue);
  }
  .brand-name {
    font-family: "Montserrat", Arial, sans-serif;
    font-weight: 800;
    color: var(--brand-blue);
    font-size: 24px;
    letter-spacing: 1px;
    text-transform: uppercase;
  }
  .contact__person { position: absolute; left: 36px; top: 118px; }
  .person-name {
    font-family: "Montserrat", Arial, sans-serif;
    font-weight: 800; font-size: 20px;
    color: var(--brand-blue); text-transform: uppercase;
  }
  .person-title { color: var(--brand-gold); font-size: 16px; margin-top: 2px; }
  .divider {
    position: absolute; left: 36px; right: 36px; top: 180px;
    height: 1px; background: var(--brand-gold);
  }
  .contact__list, .contact__place {
    position: absolute; top: 196px; list-style: none;
    color: var(--ink); font-size: 14px; line-height: 1.6;
  }
  .contact__list { left: 36px; }
  .contact__list li { display: flex; align-items: center; gap: 8px; }
  .contact__list svg { width: 14px; height: 14px; fill: var(--brand-blue); flex: none; }
  .contact__place { right: 36px; text-align: left; font-size: 14px; }
  .web-name { color: var(--brand-blue); }
  /* Brand side */
  .card--brand {
    background: var(--brand-blue);
    display: flex; flex-direction: column;
    align-items: center; justify-content: center;
    gap: 12px;
  }
  .card--brand .brand-dot { width: 96px; height: 96px; background: var(--paper); margin-bottom: 10px; }
  .card--brand .brand-name { color: var(--paper); font-size: 38px; }
  .tagline {
    font-family: "Montserrat", Arial, sans-serif;
    font-weight: 700; font-size: 17px;
    color: var(--brand-gold); text-transform: uppercase; letter-spacing: 1px;
  }
</style>
</head>
<body>
  <section class="card card--contact">
    <div class="contact__brand">
      <span class="brand-dot"></span>
      <span class="brand-name">Harborline Motors</span>
    </div>
    <div class="contact__person">
      <p class="person-name">Daniel Whitford</p>
      <p class="person-title">Managing Director</p>
    </div>
    <div class="divider"></div>
    <ul class="contact__list">
      <li><svg viewBox="0 0 24 24"><path d="M6.6 10.8a15 15 0 0 0 6.6 6.6l2.2-2.2c.3-.3.7-.4 1-.2 1.1.4 2.3.6 3.6.6.6 0 1 .4 1 1V20c0 .6-.4 1-1 1A17 17 0 0 1 3 4c0-.6.4-1 1-1h3.5c.6 0 1 .4 1 1 0 1.3.2 2.5.6 3.6.1.3 0 .7-.2 1z"/></svg>(931) 555-0148</li>
      <li><svg viewBox="0 0 24 24"><path d="M6.6 10.8a15 15 0 0 0 6.6 6.6l2.2-2.2c.3-.3.7-.4 1-.2 1.1.4 2.3.6 3.6.6.6 0 1 .4 1 1V20c0 .6-.4 1-1 1A17 17 0 0 1 3 4c0-.6.4-1 1-1h3.5c.6 0 1 .4 1 1 0 1.3.2 2.5.6 3.6.1.3 0 .7-.2 1z"/></svg>(629) 555-0173</li>
      <li><svg viewBox="0 0 24 24"><path d="M2 5h20v14H2z M2 5l10 8 10-8" fill="var(--brand-blue)" stroke="#fff" stroke-width="1.5"/></svg>harborlinemotorstn@mailbox-example.net</li>
    </ul>
    <div class="contact__place">
      <p>www.<span class="web-name">harborlinemotorstn</span>.net</p>
      <p>2741 Linden Avenue</p>
      <p>Shelbyville, TN 37162</p>
    </div>
  </section>

  <section class="card card--brand">
    <span class="brand-dot"></span>
    <span class="brand-name">Harborline Motors</span>
    <span class="tagline">Car Dealer Customer Service</span>
  </section>
</body>
</html>
```